Short term Rentals Marketing agency needs Web design.

We Need a web design for our new company based in Calgary, AB. We are a International Luxury home sharing company (short term rental properties, Villas, Boutique Hotels, Bed & Breakfast, Realtors, Mortgage Brokers). We would like to see designs that look simple, modern and professional. Colors would be bold (red, black, white). The final design should communicate something welcoming, symbolize innovation, and growth. Our goal is to form partnerships with Real Estate, Property Management, Short term Rental Clients to make their lives easier and increase revenue. Vlto Harbor Co. offers a flexible and secure way to market our clients properties while maintaining client satisfaction and amazing customer service. We like how https://plumtrellisads.ca/ is interactive (when you scroll down, text gets larger). Other similar websites for Short Term Rentals is https://www.thekeyhavenfirm.com/, https://stayvorabnb.com/, https://www.nestquill.com/, https://www.roostfinch.com/about-us/, https://lodgewardens.com. We have attached our Logo.

Target Market(s)

short term rental properties, Villas, Boutique Hotels, Bed & Breakfast, Realtors, Mortgage Brokers, property owners

Industry/Entity Type

Real Estate

Coding

Coded - Design and coding required

Number of Pages Required

5+ page

Font styles to use
Sans Serif

Requirements
Must have
• Home Page, About Us page, How it works, Services, Contact us.

We like how https://plumtrellisads.ca/ is interactive (when you scroll down, text gets larger).

We have attached our Webcopy. We would like Call to Action Buttons where they're located in the copy and page.

Must have our Logo Colors.

Other similar websites for Short Term Rentals is https://www.thekeyhavenfirm.com/, https://stayvorabnb.com/, https://www.nestquill.com/, https://www.roostfinch.com/about-us/, https://lodgewardens.com.
Nice to have
• Catchy, Interactive Home page.

Should not have
• Should not be too cluttered

```html
<!DOCTYPE html>
<html lang="en">
<head>
<meta charset="utf-8">
<title>Vlto Harbor Co. — Partner with Us</title>
<link href="https://fonts.googleapis.com/css2?family=Poppins:wght@300;400;500;600;700&display=swap" rel="stylesheet">
<style>
:root{
  --red:#e3222b;
  --red-dark:#c8141d;
  --black:#1c1c1e;
  --ink:#2a2a2a;
  --muted:#7a7a7a;
  --line:#e2e2e2;
  --soft:#f3f3f3;
  --white:#ffffff;
  --footer:#232323;
}
*{box-sizing:border-box;margin:0;padding:0}
html,body{width:1200px;height:2396px;overflow:hidden}
body{background:var(--red);font-family:'Poppins',sans-serif;color:var(--ink)}
.page{position:absolute;left:250px;top:88px;width:700px;height:2224px;background:var(--white);overflow:hidden}
section,footer,header{position:relative}
.btn{display:inline-block;background:var(--red);color:var(--white);font-size:6.5px;font-weight:500;padding:6px 14px;border-radius:12px;white-space:nowrap}
.h2{font-size:15px;font-weight:600;color:var(--black);text-align:center}
.small{font-size:5.5px;line-height:1.7;color:var(--muted)}
.more{font-size:5.5px;color:var(--black);font-weight:500}

/* hero */
.hero{height:344px;background:linear-gradient(180deg,#0c1526 0%,#1d2a44 45%,#3b3a44 80%,#241d1e 100%)}
.hero-photo{position:absolute;inset:0;background:radial-gradient(ellipse at 62% 70%,rgba(214,150,90,.45),transparent 55%),radial-gradient(ellipse at 30% 30%,rgba(40,70,120,.5),transparent 60%)}
.nav{position:absolute;top:0;left:0;right:0;height:38px;display:flex;align-items:center;padding:0 46px}
.brand{display:flex;align-items:center;gap:5px;color:var(--white);font-size:8px;font-weight:600;white-space:nowrap}
.brand i{width:9px;height:9px;border:1.5px solid var(--white);display:block}
.menu{margin-left:auto;display:flex;gap:14px;font-size:5.5px;color:var(--white);white-space:nowrap}
.menu span:first-child{color:var(--red)}
.dots{display:flex;gap:5px;margin-left:16px}
.dots b{width:6px;height:6px;border-radius:50%;background:var(--white);display:block}
.hero-copy{position:absolute;left:84px;top:100px}
.hero-copy h1{font-size:27px;line-height:1.12;font-weight:600;color:var(--white);width:260px}
.hero-copy h1 em{font-style:normal;color:var(--red)}
.hero-copy .btn{margin-top:22px}

/* intro */
.intro{height:128px;padding:30px 70px 0;text-align:center}
.intro p{font-size:5.5px;line-height:1.8;color:var(--muted);margin-bottom:10px}

/* features */
.features{height:240px;border-top:1px solid var(--line);padding-top:34px;text-align:center}
.trio{display:flex;justify-content:space-between;padding:0 110px}
.feature{width:130px}
.ring{width:30px;height:30px;border-radius:50%;border:1px solid var(--line);margin:0 auto 10px;display:flex;align-items:center;justify-content:center}
.ring.fill{background:var(--red);border-color:var(--red)}
.feature h3{font-size:7px;font-weight:500;color:var(--black);line-height:1.35;margin-bottom:6px;min-height:19px}
.feature .small{margin-bottom:6px}
.features .btn{margin-top:22px}

/* about */
.about{height:300px;display:flex;padding:20px 58px 0 58px}
.about-text{width:300px}
.about-text h2{font-size:15px;font-weight:600;color:var(--black);margin-bottom:10px}
.about-text h2::after{content:"";display:block;width:22px;height:2px;background:var(--red);margin-top:4px}
.points{display:grid;grid-template-columns:1fr 1fr;gap:14px 18px;margin:16px 0 22px}
.point{display:flex;gap:7px}
.point h4{font-size:6px;font-weight:500;color:var(--black)}
.about-photo{width:240px;height:240px;border-radius:50%;margin-left:auto;background:radial-gradient(circle at 50% 70%,#7fb9d4 0%,#3a6e8c 25%,#c9a27a 45%,#3b4a63 75%,#1e2840 100%)}

/* how */
.how{height:360px;background:var(--soft);padding-top:40px;text-align:center}
.how .sub{width:430px;margin:8px auto 28px}
.cards{display:flex;justify-content:space-between;padding:0 58px}
.card{width:184px;background:var(--white);border-top:2px solid var(--line)}
.card.active{border-top-color:var(--red)}
.card-icon{height:74px;display:flex;align-items:center;justify-content:center;border-bottom:1px solid var(--line)}
.card-body{padding:12px 16px 14px}
.card-body h3{font-size:7px;font-weight:500;color:var(--black);margin-bottom:5px}
.card-body .small{margin-bottom:6px}
.how .btn{margin-top:24px}

/* services */
.services{height:280px;padding-top:34px;text-align:center}
.services .sub{width:440px;margin:8px auto 26px}
.grid{display:grid;grid-template-columns:repeat(3,1fr);gap:22px 20px;padding:0 70px;text-align:left}
.service{display:flex;gap:8px}
.service h4{font-size:6.5px;font-weight:500;color:var(--black);margin-bottom:2px}

/* contact */
.contact{height:340px;background:var(--soft);padding-top:36px;text-align:center}
.contact .sub{width:420px;margin:8px auto 22px}
.form{width:460px;margin:0 auto;display:grid;grid-template-columns:1fr 1fr;gap:9px 14px;text-align:left}
.field{height:20px;background:var(--white);border:1px solid var(--line);font-size:5.5px;color:#aaa;padding:6px 8px}
.field.wide{grid-column:1/3;height:52px}
.contact .btn{margin-top:20px}

/* footer */
.footer{height:208px;background:var(--footer);padding:36px 58px 0;display:flex;gap:34px;color:#bdbdbd}
.col{width:130px}
.col h5{font-size:7px;font-weight:500;color:var(--white);margin-bottom:4px}
.col h5::after{content:"";display:block;width:16px;height:1.5px;background:var(--red);margin-top:4px}
.col ul{list-style:none;font-size:5.5px;line-height:2;margin-top:8px}
.col p{font-size:5.5px;line-height:1.8;margin-top:8px}
.sub-row{display:flex;margin-top:10px}
.sub-row span{flex:1;height:15px;background:#3a3a3a;font-size:5px;padding:4px 6px;color:#999}
.sub-row b{background:var(--red);color:var(--white);font-size:5px;font-weight:500;padding:4px 6px}
.social{display:flex;gap:5px;margin-top:10px}
.social i{width:9px;height:9px;border-radius:50%;background:var(--red);display:block}
.copy{position:absolute;left:58px;right:58px;bottom:14px;border-top:1px solid #3a3a3a;padding-top:8px;font-size:5px;color:#8a8a8a}
.strip{height:24px;background:var(--red-dark)}
</style>
</head>
<body>
<div class="page">
  <header class="hero">
    <div class="hero-photo" role="img" aria-label="Luxury home exterior at dusk with warm lights"></div>
    <nav class="nav">
      <div class="brand"><i></i>Vlto Harbor Co.</div>
      <div class="menu"><span>Home</span><span>About Us</span><span>How it Works</span><span>Services</span><span>Contact Us</span></div>
      <div class="dots"><b></b><b></b><b></b></div>
    </nav>
    <div class="hero-copy">
      <h1>Partner with Us &amp; Let's Start <em>Growing</em> Together!</h1>
      <span class="btn">Get Started</span>
    </div>
  </header>

  <section class="intro">
    <p>Vlto Harbor Co. is a luxury home sharing company based in Calgary, Alberta. We partner with property owners, villas, boutique hotels and realtors to market their homes and grow their revenue.</p>
    <p>We take care of listings, guests and reviews so you can relax while your property earns more every single month.</p>
  </section>

  <section class="features">
    <div class="trio">
      <div class="feature">
        <div class="ring"><svg width="14" height="14" viewBox="0 0 14 14" fill="none" stroke="#e3222b" stroke-width="1.2"><path d="M2 7 7 2l5 5M3.5 6v6h7V6"/></svg></div>
        <h3>Increase Your Revenue Without the Hassle</h3>
        <p class="small">We handle every detail so your property stays booked and profitable.</p>
        <span class="more">Read More</span>
      </div>
      <div class="feature">
        <div class="ring fill"><svg width="14" height="14" viewBox="0 0 14 14" fill="none" stroke="#fff" stroke-width="1.2"><circle cx="7" cy="7" r="5"/><path d="M7 4v3l2 2"/></svg></div>
        <h3>Flexible, Constant Support</h3>
        <p class="small">We handle every detail so your property stays booked and profitable.</p>
        <span class="more">Read More</span>
      </div>
      <div class="feature">
        <div class="ring"><svg width="14" height="14" viewBox="0 0 14 14" fill="none" stroke="#e3222b" stroke-width="1.2"><rect x="2" y="3" width="10" height="9"/><path d="M2 6h10M5 1.5v3M9 1.5v3"/></svg></div>
        <h3>Manage Your Rates and Bookings</h3>
        <p class="small">We handle every detail so your property stays booked and profitable.</p>
        <span class="more">Read More</span>
      </div>
    </div>
    <span class="btn">Get Started</span>
  </section>

  <section class="about">
    <div class="about-text">
      <h2>About Us</h2>
      <p class="small">Founded in Calgary, we help owners turn homes into thriving short term rentals. Our team blends local knowledge with modern marketing to deliver real results.</p>
      <div class="points">
        <div class="point"><svg width="12" height="12" viewBox="0 0 12 12" fill="none" stroke="#e3222b" stroke-width="1"><path d="M6 11s4-3.5 4-6.5a4 4 0 0 0-8 0C2 7.5 6 11 6 11z"/><circle cx="6" cy="4.5" r="1.3"/></svg><div><h4>Local Experts</h4><p class="small">Trusted care for every stay.</p></div></div>
        <div class="point"><svg width="12" height="12" viewBox="0 0 12 12" fill="none" stroke="#e3222b" stroke-width="1"><rect x="1.5" y="3" width="9" height="6.5"/><path d="M1.5 5h9"/></svg><div><h4>Secure Payments</h4><p class="small">Trusted care for every stay.</p></div></div>
        <div class="point"><svg width="12" height="12" viewBox="0 0 12 12" fill="none" stroke="#e3222b" stroke-width="1"><path d="M3 2h2l1 2.5-1.3 1a6 6 0 0 0 2.8 2.8l1-1.3L11 8v2a1 1 0 0 1-1 1A9 9 0 0 1 2 3a1 1 0 0 1 1-1z"/></svg><div><h4>Guest Support</h4><p class="small">Trusted care for every stay.</p></div></div>
        <div class="point"><svg width="12" height="12" viewBox="0 0 12 12" fill="none" stroke="#e3222b" stroke-width="1"><path d="M1.5 10 5 6.5l2 2L10.5 4M8 4h2.5v2.5"/></svg><div><h4>Growth Focused</h4><p class="small">Trusted care for every stay.</p></div></div>
      </div>
      <span class="btn">Learn More</span>
    </div>
    <div class="about-photo" role="img" aria-label="Luxury villa with pool lit in the evening"></div>
  </section>

  <section class="how">
    <h2 class="h2">How It Works</h2>
    <p class="small sub">Three simple steps to start earning more from your property with our team.</p>
    <div class="cards">
      <div class="card active">
        <div class="card-icon"><svg width="22" height="22" viewBox="0 0 22 22" fill="none" stroke="#e3222b" stroke-width="1.2"><rect x="3" y="4" width="16" height="15"/><path d="M3 9h16M7 2v4M15 2v4"/></svg></div>
        <div class="card-body"><h3>Book a Consultation</h3><p class="small">Tell us about your home and goals so we can plan.</p><span class="more">Read More</span></div>
      </div>
      <div class="card">
        <div class="card-icon"><svg width="22" height="22" viewBox="0 0 22 22" fill="none" stroke="#e3222b" stroke-width="1.2"><circle cx="10" cy="10" r="6"/><path d="m14.5 14.5 5 5"/></svg></div>
        <div class="card-body"><h3>Optimize Your Property</h3><p class="small">Tell us about your home and goals so we can plan.</p><span class="more">Read More</span></div>
      </div>
      <div class="card">
        <div class="card-icon"><svg width="22" height="22" viewBox="0 0 22 22" fill="none" stroke="#e3222b" stroke-width="1.2"><path d="M3 11 11 3l8 8M5 9.5V19h12V9.5"/><path d="M9 19v-5h4v5"/></svg></div>
        <div class="card-body"><h3>Start Hosting Bookings</h3><p class="small">Tell us about your home and goals so we can plan.</p><span class="more">Read More</span></div>
      </div>
    </div>
    <span class="btn">Get Started Today</span>
  </section>

  <section class="services">
    <h2 class="h2">Our Services</h2>
    <p class="small sub">We offer complete management and marketing services for short term rentals of every size.</p>
    <div class="grid">
      <div class="service"><svg width="13" height="13" viewBox="0 0 13 13" fill="none" stroke="#e3222b" stroke-width="1"><rect x="1.5" y="3.5" width="10" height="7.5"/><circle cx="6.5" cy="7.2" r="2"/><path d="M4.5 3.5 5.5 2h2l1 1.5"/></svg><div><h4>Interior and Exterior Photography</h4><p class="small">Professional care that keeps guests happy and returning.</p><span class="more">Read More</span></div></div>
      <div class="service"><svg width="13" height="13" viewBox="0 0 13 13" fill="none" stroke="#e3222b" stroke-width="1"><rect x="2" y="2.5" width="9" height="9"/><path d="M2 5h9M4.5 8l1.5 1.5 2.5-3"/></svg><div><h4>Direct Bookings</h4><p class="small">Professional care that keeps guests happy and returning.</p><span class="more">Read More</span></div></div>
      <div class="service"><svg width="13" height="13" viewBox="0 0 13 13" fill="none" stroke="#e3222b" stroke-width="1"><path d="M2 11.5V7M5 11.5V4.5M8 11.5V6M11 11.5V2"/></svg><div><h4>Financial Reporting</h4><p class="small">Professional care that keeps guests happy and returning.</p><span class="more">Read More</span></div></div>
      <div class="service"><svg width="13" height="13" viewBox="0 0 13 13" fill="none" stroke="#e3222b" stroke-width="1"><path d="M2 6.5 6.5 2 11 6.5M3.5 5v6.5h6V5"/></svg><div><h4>Cleaning and Inspections</h4><p class="small">Professional care that keeps guests happy and returning.</p><span class="more">Read More</span></div></div>
      <div class="service"><svg width="13" height="13" viewBox="0 0 13 13" fill="none" stroke="#e3222b" stroke-width="1"><path d="M2 2.5h9v6.5H5L2.5 11V9H2z"/></svg><div><h4>Customer Communication</h4><p class="small">Professional care that keeps guests happy and returning.</p><span class="more">Read More</span></div></div>
      <div class="service"><svg width="13" height="13" viewBox="0 0 13 13" fill="none" stroke="#e3222b" stroke-width="1"><circle cx="6.5" cy="6.5" r="4.5"/><path d="M6.5 4v2.5l1.8 1.5"/></svg><div><h4>Calendar Adjustments</h4><p class="small">Professional care that keeps guests happy and returning.</p><span class="more">Read More</span></div></div>
    </div>
  </section>

  <section class="contact">
    <h2 class="h2">Contact us</h2>
    <p class="small sub">Ready to grow? Send us a message and a member of our team will reply within one business day.</p>
    <div class="form">
      <div class="field">Name</div>
      <div class="field">Email</div>
      <div class="field">Phone</div>
      <div class="field">Subject</div>
      <div class="field wide">Message</div>
    </div>
    <span class="btn">Submit Message</span>
  </section>

  <footer class="footer">
    <div class="col"><h5>About Us</h5><p>Luxury home sharing partners helping owners grow across Canada.</p></div>
    <div class="col"><h5>Company Links</h5><ul><li>Home</li><li>About Us</li><li>How it Works</li><li>Services</li><li>Contact</li></ul></div>
    <div class="col"><h5>Services</h5><ul><li>Photography</li><li>Direct Bookings</li><li>Reporting</li><li>Cleaning</li></ul></div>
    <div class="col"><h5>Newsletter</h5><div class="sub-row"><span>Your email</span><b>Subscribe</b></div><div class="social"><i></i><i></i><i></i><i></i><i></i></div></div>
    <div class="copy">© 2024 Vlto Harbor Co. All rights reserved.</div>
  </footer>
  <div class="strip"></div>
</div>
</body>
</html>
```